QMB Vane Works

- Brochure design

Target Market(s)

Granite and Quartz

Font styles to use
Sans Serif

Colors

Designer to choose colors to be used in the design.

Requirements
Must have
• I post the instruction file below
Nice to have
Should not have

```html
<!DOCTYPE html>
<html lang="en">
<head>
<meta charset="utf-8">
<title>QMB Vane Works – Vanity Tops Brochure Spread</title>
<link href="https://fonts.googleapis.com/css2?family=Source+Sans+3:wght@400;600&display=swap" rel="stylesheet">
<style>
:root{
  --bg:#ffffff;
  --paper:#f2f2f2;
  --band:#2f2a28;
  --ink:#222222;
  --muted:#555555;
  --head-row:#5a5a5a;
  --row:#dcdcdc;
  --row-alt:#e8e8e8;
  --rule:#9a9a9a;
}
*{box-sizing:border-box;margin:0;padding:0}
html,body{width:1200px;height:900px;overflow:hidden;background:var(--bg);font-family:"Source Sans 3",sans-serif;color:var(--ink)}
.spread{position:absolute;left:40px;top:39px;width:940px;height:690px;transform:scale(1.19);transform-origin:0 0;display:flex;box-shadow:0 6px 18px rgba(0,0,0,.18)}
.page{position:relative;width:470px;height:690px;background:var(--paper);overflow:hidden}
.page--left{border-right:1px solid #d8d8d8}
.band{position:absolute;left:0;top:0;width:100%;height:116px;background:var(--band)}
.band::after{content:"";position:absolute;left:0;right:0;top:97px;height:1px;background:#e8e8e8}
.brand{position:absolute;left:37px;top:44px;color:#fff;font-size:24px;font-weight:400;letter-spacing:.5px}
.tagline{position:absolute;left:37px;top:76px;color:#ddd;font-size:8px}
.section-title{position:absolute;left:37px;top:132px;font-size:14px;font-weight:400}
.section-rule{position:absolute;left:37px;top:151px;width:403px;height:1px;background:var(--rule)}
.sizes-label{position:absolute;left:38px;top:166px;font-size:7.5px}
.sizes{position:absolute;left:39px;top:184px;width:146px;border-collapse:collapse;font-size:7px}
.sizes td{border:1px solid #444;height:15px;text-align:center;background:#fff}
.photo{position:absolute}
.photo--kitchen{left:39px;top:304px;width:146px;height:156px;background:linear-gradient(135deg,#6b3e22,#b58a5c 55%,#4a2a18)}
.photo--bath{left:199px;top:168px;width:133px;height:290px;background:linear-gradient(160deg,#5a4d44,#c9c2b6 45%,#3a3030)}
.drawing{position:absolute;left:345px;width:97px;height:52px;background:#e2e2e2;border:1px solid #bbb}
.drawing-label{position:absolute;left:345px;width:97px;text-align:center;font-size:6.5px}
.swatch{position:absolute;width:72px;height:40px;border-radius:2px}
.swatch-label{position:absolute;width:90px;text-align:center;font-size:6.5px}
.footer-num{position:absolute;top:665px;font-size:12px}
.footer-url{position:absolute;top:668px;font-size:7px}
.table-title{position:absolute;left:33px;width:405px;text-align:center;font-size:10px}
.spec{position:absolute;left:33px;width:405px;border-collapse:collapse;font-size:6.6px;table-layout:fixed}
.spec th{background:var(--head-row);color:#eee;font-weight:400;height:12px;text-align:center}
.spec td{background:var(--row);vertical-align:top;padding:3px 3px 2px;text-align:center;line-height:1.3}
.spec tr:nth-child(odd) td{background:var(--row-alt)}
.spec td.label{text-align:left;padding-left:6px}
.spec td.desc{text-align:left;padding-right:4px}
.col-label{width:95px}.col-val{width:47px}
</style>
</head>
<body>
<div class="spread">
  <section class="page page--left">
    <div class="band"></div>
    <div class="brand">QMB Vane Works</div>
    <div class="tagline">Naturally Beautiful, Premium Quality</div>

    <h2 class="section-title">VANITY TOPS</h2>
    <div class="section-rule"></div>
    <p class="sizes-label">American Standard Sizes</p>
    <table class="sizes">
      <tr><td>25” X 22” X 3/4”</td><td>25” X 22” X 3CM</td></tr>
      <tr><td>31” X 22” X 3/4”</td><td>33” X 22” X 3CM</td></tr>
      <tr><td>37” X 22” X 3/4”</td><td>37” X 22” X 3CM</td></tr>
      <tr><td>43” X 22” X 3/4”</td><td>43” X 22” X 3CM</td></tr>
      <tr><td>49” X 22” X 3/4”</td><td>49” X 22” X 3CM</td></tr>
      <tr><td>61” X 22” X 3/4”</td><td>61” X 22” X 3CM</td></tr>
      <tr><td>73” X 22” X 3/4”</td><td>73” X 22” X 3CM</td></tr>
    </table>

    <div class="photo photo--kitchen" role="img" aria-label="Kitchen island with granite countertop and sink"></div>
    <div class="photo photo--bath" role="img" aria-label="Kitchen with white stone counter, sink and pendant lights"></div>

    <div class="drawing" style="top:168px" role="img" aria-label="Vanity top diagram with oval sink"></div>
    <div class="drawing-label" style="top:229px">Vanity Top</div>
    <div class="drawing" style="top:266px" role="img" aria-label="Vanity top diagram with square sink"></div>
    <div class="drawing-label" style="top:327px">Vanity Top</div>
    <div class="drawing" style="top:361px" role="img" aria-label="Banjo vanity top diagram"></div>
    <div class="drawing-label" style="top:425px">Banjo Vanity Top</div>

    <div class="swatch" style="left:44px;top:482px;background:linear-gradient(135deg,#fafafa,#dcdcdc)" role="img" aria-label="Crystal White Quartz vanity top"></div>
    <div class="swatch-label" style="left:37px;top:540px">Crystal White Quartz</div>
    <div class="swatch" style="left:130px;top:480px;background:linear-gradient(135deg,#c8c6c2,#8f8c88)" role="img" aria-label="Crystal Grey Quartz vanity top"></div>
    <div class="swatch-label" style="left:123px;top:538px">VT-Crystal Grey Quartz</div>
    <div class="swatch" style="left:215px;top:480px;background:linear-gradient(135deg,#e6e6e6,#b5b5b5)" role="img" aria-label="Carrara White vanity top"></div>
    <div class="swatch-label" style="left:206px;top:536px">VT-Carrara White</div>
    <div class="swatch" style="left:294px;top:478px;background:linear-gradient(135deg,#f3e6cf,#d9c7a4)" role="img" aria-label="Creme Marfil vanity top"></div>
    <div class="swatch-label" style="left:286px;top:534px">VT-Creme Marfil</div>
    <div class="swatch" style="left:370px;top:476px;background:linear-gradient(135deg,#6a5748,#3e322a)" role="img" aria-label="Tan Brown vanity top"></div>
    <div class="swatch-label" style="left:362px;top:532px">VT-Tan Brown</div>

    <div class="swatch" style="left:44px;top:562px;background:linear-gradient(135deg,#d8b88e,#a98458)" role="img" aria-label="New Venetian Gold vanity top"></div>
    <div class="swatch-label" style="left:37px;top:620px">VT-New Venetian Gold</div>
    <div class="swatch" style="left:130px;top:562px;background:linear-gradient(135deg,#2a2a2a,#0d0d0d)" role="img" aria-label="Mongolian Black vanity top"></div>
    <div class="swatch-label" style="left:123px;top:618px">VT-Mongolian Black</div>
    <div class="swatch" style="left:215px;top:558px;background:linear-gradient(135deg,#e8d7a8,#c4ad76)" role="img" aria-label="Golden Garnet vanity top"></div>
    <div class="swatch-label" style="left:206px;top:616px">VT-Golden Garnet</div>
    <div class="swatch" style="left:297px;top:556px;background:linear-gradient(135deg,#d6b996,#a8866a)" role="img" aria-label="Santa Cecilia Dark vanity top"></div>
    <div class="swatch-label" style="left:288px;top:614px">VT-Santa Cecilia Dark</div>

    <div class="footer-num" style="left:13px">09</div>
    <div class="footer-url" style="left:38px">www.QMBVANEWORKS.com</div>
  </section>

  <section class="page page--right">
    <div class="band"></div>

    <h3 class="table-title" style="top:133px">Physical Attributes</h3>
    <table class="spec" style="top:146px">
      <colgroup><col class="col-label"><col class="col-val"><col class="col-val"><col class="col-val"><col></colgroup>
      <tr><th></th><th>Marble</th><th>Granite</th><th>Quartz</th><th></th></tr>
      <tr><td class="label">Melt Point (0F)</td><td>2,442</td><td>1,260</td><td>1,270</td><td></td></tr>
      <tr><td class="label">Source</td><td>Nature</td><td>Nature</td><td>Human Made</td><td></td></tr>
      <tr style="height:43px"><td class="label">Hardness</td><td>4</td><td>6</td><td>7</td><td class="desc">Quartz countertops are made by 93% natural quartz stone with 7% resin binder. This creates an extremely hard stone that is stronger the granite or marble.</td></tr>
      <tr style="height:66px"><td class="label">Color Consistenct</td><td>No</td><td>No</td><td>Yes</td><td class="desc">Each marble and granite is unique. If you use 2 separate pieces for islands and countertop, you might experience the color difference. Black granite dyes charge and the appearance of the counter may not be the same as you initially installed. Quartz is human made, and the color is consistent throughout the entire slab.</td></tr>
    </table>

    <h3 class="table-title" style="top:314px">Durability</h3>
    <table class="spec" style="top:328px">
      <colgroup><col class="col-label"><col class="col-val"><col class="col-val"><col class="col-val"><col></colgroup>
      <tr><th></th><th>Marble</th><th>Granite</th><th>Quartz</th><th></th></tr>
      <tr><td class="label">Scratch Resistance</td><td>Good</td><td>Good</td><td>Good</td><td></td></tr>
      <tr style="height:62px"><td class="label">Household Chemicals Stain Resistance (Wine, Vinegar, Soap, Mold, etc.)</td><td>Poor</td><td>Good</td><td>Good</td><td class="desc">Granite and marble are both porous stones. If you spill the wine on granite or marble, the wine can sink into the stone and potentially permanently stain the stone. Quartz is human made stones, and it never requires sealing. Quartz is very stain resistant.</td></tr>
      <tr><td class="label">Heat Resistance</td><td>Good</td><td>Good</td><td>Good</td><td></td></tr>
      <tr><td class="label">Abration</td><td>Poor</td><td>Good</td><td>Good</td><td></td></tr>
    </table>

    <h3 class="table-title" style="top:465px">Maintance</h3>
    <table class="spec" style="top:478px">
      <colgroup><col class="col-label"><col class="col-val"><col class="col-val"><col class="col-val"><col></colgroup>
      <tr><th></th><th>Marble</th><th>Granite</th><th>Quartz</th><th>Descriptions</th></tr>
      <tr style="height:36px"><td class="label">Easy To Clean</td><td>No</td><td>Yes</td><td>Yes</td><td class="desc">It’s easy to clean the quartz, compared to marble and granite. The quartz washes off with soap and water and looks as good as new.</td></tr>
      <tr><td class="label">Easy To Repair</td><td>Poor</td><td>Fair</td><td>Good</td><td></td></tr>
      <tr style="height:52px"><td class="label">Regular Maintance</td><td>Yes</td><td>Yes</td><td>No</td><td class="desc">Granite and marble countertops must by sealed regularly (Once a year) to prevent staining. The maintenance adds to the cost of the countertops. Quartz doesn’t require sealing or regular maintenance.</td></tr>
    </table>

    <h3 class="table-title" style="top:605px">Value</h3>
    <table class="spec" style="top:618px">
      <colgroup><col class="col-label"><col class="col-val"><col class="col-val"><col class="col-val"><col></colgroup>
      <tr><th></th><th>Marble</th><th>Granite</th><th>Quartz</th><th></th></tr>
      <tr><td class="label">Price Per sqft</td><td>$$$</td><td>$$</td><td>$$$$</td><td class="desc">Quartz is less expensive</td></tr>
    </table>

    <div class="footer-url" style="right:34px">www.QMBVANEWORKS.com</div>
    <div class="footer-num" style="right:14px">10</div>
  </section>
</div>
</body>
</html>
```